Where Quiet Rivers Carry Us

I have a previously designed book cover, and although I am mostly happy with it, I do not care for the photo on the cover of the book. I would like to keep the fonts and scrollwork on the current book cover (the brown outer edge is optional).
I prefer a Christian focus with a soft, gentle, grieving, trusting feeling of a mother as God leads without the typical religious symbols (ie: huge hands, overwhelming crosses, Heaven opening). Softly toned or small Christian icons would be acceptable.
The book dimensions are 5.5 X 8.5 and the spine is 1/2" thick.
Original book cover is here: http://wherequietriverscarryus.pinebrookpages.net/p/free-books.html
Back cover book description (two photos and the logo for the back cover can be found below) :
For I am the Lord your God who takes hold of your right hand and says to you, "Do not fear, I will help you." Isaiah 41:13
One day you were here, Colby, the next you were at the throne of God. How I long to know what heaven is like so I can envision where you are. Are you talking to Gideon about the battles of old? Are you asking Paul about the stonings, the scales, and the shipwrecks? Or are you still just standing in awe of the God and Savior that your mother could never have come close to describing to you? How I long to stand in awe with you, praising the God who gives and takes away. Just like I told you all those times when you were here with us, "If you go first, I'll see you when I get there, my son." Love you, Mom
On Friday, February 18, 2011, God did the unthinkable in our lives: He chose to take our 12-year-old son, Colby, home to heaven in a skiing accident. It is only considered the unthinkable because our plans are not God's plans and our ways are not God's ways. Follow along on my journey through the valley of the shadow of death as my Savior, Jesus Christ, leads me.
(Author info)
Janna L. Voskuilen lives on a small farm in northern Wisconsin with her husband, Dale, and their children. Experiencing the tragic death of her son has caused her to draw closer to God as He leads her down an unexpected path to know Him better.
I have updated the back cover details to include the exact words for the back cover as well as two photos and a logo. Thank you, designers, for sharing your creativity!
Reason: Still looking for the perfect book cover!
Reason: Still looking for the perfect design!
Working on final revisions!

```html
<!DOCTYPE html>
<html lang="en">
<head>
<meta charset="utf-8">
<title>Where Quiet Rivers Carry Us — Front Cover</title>
<link rel="stylesheet" href="https://fonts.googleapis.com/css2?family=Pinyon+Script&family=Cormorant+Garamond:wght@500&display=swap">
<style>
  :root {
    --backdrop: #f4f4f4;
    --frame-dark: #5e4122;
    --frame-mid: #9a7443;
    --frame-light: #c9a86c;
    --sky-glow: #fbf1b4;
    --sky-warm: #efd98e;
    --lake: #b8a675;
    --lake-deep: #8e825e;
    --dock: #6f5a3e;
    --dock-dark: #4c3b27;
    --title-red: #7c1d10;
    --author-white: #f7f1e6;
  }
  * { margin: 0; padding: 0; box-sizing: border-box; }
  html, body {
    width: 1200px;
    height: 1000px;
    overflow: hidden;
    background: var(--backdrop);
  }
  .canvas {
    position: relative;
    width: 1200px;
    height: 1000px;
  }
  .book-cover {
    position: absolute;
    left: 320px;
    top: 67px;
    width: 560px;
    height: 866px;
    background:
      radial-gradient(ellipse at 30% 20%, var(--frame-light) 0%, transparent 55%),
      radial-gradient(ellipse at 80% 85%, var(--frame-light) 0%, transparent 50%),
      linear-gradient(135deg, var(--frame-mid), var(--frame-dark));
    box-shadow: 0 8px 24px rgba(0,0,0,0.18);
    overflow: hidden;
  }
  .cover-photo {
    position: absolute;
    left: 27px;
    right: 27px;
    top: 17px;
    bottom: 0;
    background: linear-gradient(180deg,
      var(--sky-warm) 0%,
      var(--sky-glow) 22%,
      var(--sky-warm) 38%,
      var(--lake) 48%,
      var(--lake-deep) 70%,
      var(--lake) 76%,
      var(--dock) 84%,
      var(--dock-dark) 100%);
  }
  .cover-photo::after {
    content: "";
    position: absolute;
    inset: 0;
    background: radial-gradient(circle at 25% 22%, rgba(255,250,210,0.85) 0%, rgba(255,250,210,0) 45%);
  }
  .title {
    position: absolute;
    left: 42px;
    top: 322px;
    font-family: "Pinyon Script", cursive;
    font-weight: 400;
    font-size: 68px;
    line-height: 74px;
    color: var(--title-red);
  }
  .title span { display: block; white-space: nowrap; }
  .author {
    position: absolute;
    left: 0;
    right: 0;
    top: 796px;
    text-align: center;
    font-family: "Cormorant Garamond", serif;
    font-weight: 500;
    font-size: 21px;
    letter-spacing: 0.3em;
    text-transform: uppercase;
    color: var(--author-white);
  }
</style>
</head>
<body>
  <main class="canvas">
    <section class="book-cover">
      <div class="cover-photo" role="img" aria-label="Sun-washed photograph of a woman seen from behind on a wooden dock by a lake, holding a bunch of pale balloons against a glowing sky"></div>
      <h1 class="title">
        <span>Where</span>
        <span>Quiet Rivers</span>
        <span>Carry Us</span>
      </h1>
      <p class="author">Janna L. Voskuilen</p>
    </section>
  </main>
</body>
</html>
```